'Ormel Property Development' Business Card

Business Card Features:

High Quality (potentially textured) thick card - preference is white textured card

Logo (supplied)

We plan to use the vertical logo as the main logo. But i am happy for people to use either if they find it works better for the design of the card.

The building icon and also the insert to the 'E' is in a metallic finish, i think this should be finished in a metallic embossed or raised style.
Updates

Please note i have attached both a horizontal and Vertical Logo for your reference. We plan to use the vertical logo as the main logo. But i am happy for people to use either if they find it works better for the design of the card.

Please note i am considering having the cards made on stainless steel. This introduces the option of having cut outs in the card and etching or printing for the design. If you have a good concept for this please submit.

http://www.tinquarry.example/black-metal-cards# this is a site that makes the metal cards to offer some direction . . . . Please note i am basic the selection o the best design, if that means normal print cards on paper then this is what i will choose. But there are some great options with the metal. Thanks.

Industry/Entity Type

Building

Requirements
Must have
• Helvetica font to details side of card - logo as supplied to opposite side.

Card Details:

Darrow Pketts
Managing Director

+61 487 263 518
+61 3 6172 4809

PO Box 73
Bentleigh, VIC 3024

darrow@ormel.example

www.ormel.example

```html
<!DOCTYPE html>
<html lang="en">
<head>
<meta charset="utf-8">
<title>Ormel Property Development – Business Card</title>
<link href="https://fonts.googleapis.com/css2?family=Arimo:wght@400;700&display=swap" rel="stylesheet">
<style>
  :root {
    --backdrop: #d6d6d6;
    --card-white: #ffffff;
    --card-black: #0b0b0b;
    --ink: #111111;
    --ink-soft: #3a3a3a;
    --metal: #9a9a9a;
    --metal-light: #c4c4c4;
    --metal-dark: #6d7073;
  }
  * { margin: 0; padding: 0; box-sizing: border-box; }
  html, body {
    width: 1200px;
    height: 926px;
    overflow: hidden;
  }
  body {
    background: var(--backdrop);
    font-family: "Arimo", "Helvetica Neue", Helvetica, Arial, sans-serif;
    color: var(--ink);
    position: relative;
  }
  .card {
    position: absolute;
    top: 298px;
    width: 540px;
    height: 330px;
    box-shadow: 0 8px 24px rgba(0,0,0,0.22);
    overflow: hidden;
  }
  .card--front {
    left: 40px;
    background: var(--card-white);
  }
  .card--back {
    left: 620px;
    background: radial-gradient(ellipse at 50% 45%, #2b2b2b 0%, var(--card-black) 62%);
  }

  /* Front: ribbon logo band */
  .ribbon {
    position: absolute;
    left: 0;
    top: 106px;
    width: 250px;
    height: 80px;
  }
  .ribbon svg { position: absolute; inset: 0; }
  .ribbon__mark {
    position: absolute;
    left: 24px;
    top: 26px;
    width: 28px;
    height: 28px;
    background: var(--metal-light);
  }
  .ribbon__divider {
    position: absolute;
    left: 66px;
    top: 14px;
    width: 1px;
    height: 52px;
    background: var(--metal);
  }
  .ribbon__name {
    position: absolute;
    left: 78px;
    top: 20px;
    width: 140px;
    font-weight: 400;
    font-size: 16px;
    line-height: 1.2;
    color: var(--metal-light);
  }

  /* Front: details */
  .details {
    position: absolute;
    left: 290px;
    top: 72px;
  }
  .details__name {
    font-weight: 700;
    font-size: 29px;
    line-height: 1;
    color: var(--ink);
  }
  .details__role {
    font-weight: 700;
    font-size: 12px;
    margin-top: 4px;
    color: var(--ink-soft);
  }
  .details__contacts {
    list-style: none;
    margin-top: 20px;
    font-size: 14px;
    line-height: 1.66;
    color: var(--ink-soft);
  }

  /* Back: centred logo */
  .brand {
    position: absolute;
    left: 0;
    right: 0;
    top: 92px;
    text-align: center;
  }
  .brand__mark {
    display: block;
    width: 62px;
    height: 62px;
    margin: 0 auto 16px;
    background: linear-gradient(135deg, var(--metal-light), var(--metal));
  }
  .brand__name {
    font-weight: 700;
    font-size: 25px;
    letter-spacing: 1px;
    line-height: 1.25;
    color: var(--metal-dark);
  }
</style>
</head>
<body>

  <section class="card card--front" aria-label="Business card front">
    <div class="ribbon">
      <svg width="250" height="80" viewBox="0 0 250 80" aria-hidden="true">
        <polygon points="0,0 250,0 232,40 250,80 0,80" fill="#0b0b0b"/>
      </svg>
      <span class="ribbon__mark"></span>
      <span class="ribbon__divider"></span>
      <p class="ribbon__name">Ormel Property Development</p>
    </div>

    <div class="details">
      <h1 class="details__name">Darrow Pketts</h1>
      <p class="details__role">Managing Director</p>
      <ul class="details__contacts">
        <li>+61 487 263 518</li>
        <li>+61 3 6172 4809</li>
        <li>www.ormel.example</li>
        <li>darrow@ormel.example</li>
        <li>PO BOX 73 Bentleigh, VIC 3024</li>
      </ul>
    </div>
  </section>

  <section class="card card--back" aria-label="Business card back">
    <div class="brand">
      <span class="brand__mark"></span>
      <p class="brand__name">Ormel Property Development</p>
    </div>
  </section>

</body>
</html>
```